We need a range of stationery items designed for our active, community-orientated, out-going, all-age, family-friendly church in central Auckland, New Zealand.
We want to refresh and modernize the branding/images for Kerrowby Baptist Church itself so this image reflects who we are and our values.
Our church is located on a very busy intersection in the heart of a multi-ethnic local community. A number of churches and other groups use our site so we have branded our site as "The Lantern Yard". We have an existing logo for "The Lantern Yard" (see attached).
We would like you to design 4 items: a Letterhead, a With Compliments slip, a Business Card, and the Front Cover of our church newsletter, but we've included a request for an Email signature as an optional extra for this brief.
Organisation Details:
Name: Kerrowby Baptist Church
Postal Address: PO Box 53081, Kerrowby, Auckland 1832
Email: office@kerrowbychapel.org.nz
Phone: 09 361 4507
Web: www.kerrowbychapel.org.nz (current website will be changed)
Position Statement: "a place of hope, belonging and worship"
Fonts:
The fonts for the "The Lantern Yard" logo are Futura Medium BT and Futura Lt BT. We would like the Futura font family used in the designs but feel free to add other fonts as appropriate (preferably True Type open source ones).
Colours:
Our current external signage colours are Dark Grey (Tovalin Coatings 'Slatewick' - RGB 57-55-53 ) and orange ( Tovalin 'Firebloom' - RGB 255-82-0 ). These are the colours for 'The Lantern Yard' which is our site. As we have other churches using our premises also we are looking to create a separate but complimentary identity for Kerrowby Baptist Church with a different colour set. We would ideally like a primary colour, a complimentary colour and an offset colour.
Design:
For the Kerrowby Baptist Church stationary we want the design to incorporate some of the elements of the 'Lantern Yard' particularly the extended 'T' device, so that we develop a separate identity but in the same family. We would like something that will look good for a number of years, rather than something that will date quickly in a year or two as fashions change.
PROJECTS
1. Letterhead
Finished size A4 (210 mm wide x 297mm tall)
This will become a template in DocuPad. It will be printed in colour on our office photocopier so it must have a 5mm white border around the entire outside edge of the A4 page. "The Lantern Yard" logo needs to be incorporated in some form on the page.
2. With Compliments slip
Finished size 210 mm wide x 99 mm tall
This will be printed in colour on our office photocopier so it must have a 5mm white border around the entire outside edge of the slip. We will print these slips 3-up on an A4 page. The actual design space will be 200mm x 89mm. It is envisaged that this slip will use the same elements as the letterhead design. Please supply two versions, with and without the words "With Compliments".
3. Business Card
Finished size 90 mm wide by 55 mm tall.
This will be printed by commercial printers so colours can run to the edge of the card. Your Kerrowby Baptist Logo with the extended 'T' devise will need to feature on this.
4. Front Cover of Church Newsletter
Finished size 100 mm wide x 210 mm tall.
Our newsletter is printed in landscape on A4 paper and is folded twice.
It will be printed in colour on our office photocopier so it will need to have a minimum 5mm white border on all 4 sides. Attractive inviting colours preferred.
Needs to have:
- a place for the words Sunday and a date (which will change each Sunday)
- your Kerrowby Baptist Logo with the extended 'T' devise
- the words Sundays @ 10am
- the words ""a place of hope, belonging and worship"
- optional - "The Lantern Yard" logo (background does not need to be black)
5. Email Signature - optional extra
Not too large but something that will enable those receiving emails to instantly recognize who the email is from. Needs to include your Kerrowby Baptist logo, the name of the person, their position and our contact details.
Reason: We are extending the deadline on this project in order to encourage a broader range of designs, both from those who have already submitted designs and from those who are considering entering our competition. We'd love to see what you have to offer so please do submit your designs.
Re: Stationery for Kerrowby Baptist Church
Thanks to all the designers who have submitted designs for our competition so far. We have refrained from requesting a whole lot of tweaks to individual designs out of respect for your time as we understand that you are all busy professionals and that design competitions like this are just one way that you pitch for new business.
We would though like to offer some general comments on the submissions that we have seen so far. One thing that we would definitely like to arrive at via this process is to decide on a colour scheme. For this, as per the brief notes ( but possibly obscured by some of the other detail ) we want to have a primary colour and an offset colour and also an accent colour in the pallet.
Another thing that we maybe didn't make clear enough is that the colours for the identity of the site, known as The Lantern Yard, uses dark grey and orange but that we wanted to develop a separate but related identity for Kerrowby Baptist Church that meets there as we also now have other congregations that use our buildings.
One of the keys for the new identity will be the new colour pallet which we wanted to steer away from the darker tones that we used for the site branding. Therefore we would very much like to see your suggestions one or two secondary colours along with the primary brand colour if possible please.
Thank you all once again.
Kind regards

```html
<!DOCTYPE html>
<html lang="en">
<head>
<meta charset="utf-8">
<title>The Lantern Yard – Stationery Set</title>
<link href="https://fonts.googleapis.com/css2?family=Jost:wght@300;400;500&family=Yellowtail&display=swap" rel="stylesheet">
<style>
  :root {
    --stage: #ababab;
    --paper: #ffffff;
    --brand-red: #b5292a;
    --charcoal: #333335;
    --ink-light: #f2f2f2;
  }
  * { box-sizing: border-box; margin: 0; padding: 0; }
  html, body { width: 1200px; height: 640px; overflow: hidden; background: var(--stage); }
  body { position: relative; font-family: "Jost", "Futura", sans-serif; color: var(--charcoal); }
  .piece { position: absolute; background: var(--paper); overflow: hidden; }

  .wordmark { font-weight: 500; letter-spacing: 0.06em; line-height: 0.95; text-transform: uppercase; }
  .wordmark span { display: block; }
  .wordmark .wm-top { padding-left: 0.55em; }

  .contact { list-style: none; font-weight: 400; line-height: 1.35; }
  .contact li { display: flex; align-items: center; gap: 3px; white-space: nowrap; }
  .contact svg { flex: none; fill: var(--brand-red); }

  /* Newsletter cover */
  .newsletter { left: 27px; top: 42px; width: 227px; height: 477px; }
  .newsletter-frame { position: absolute; left: 11px; top: 11px; width: 205px; height: 454px; border: 2px solid var(--brand-red); border-top: none; }
  .newsletter-hero { position: absolute; left: 11px; top: 11px; width: 205px; height: 200px; }
  .newsletter .wordmark { position: absolute; left: 26px; top: 282px; font-size: 21px; color: var(--charcoal); }
  .newsletter-service { position: absolute; left: 70px; top: 363px; font-size: 12px; font-weight: 500; color: var(--brand-red); }
  .newsletter-date { position: absolute; left: 11px; width: 205px; top: 389px; text-align: center; font-size: 15.5px; font-weight: 300; color: var(--brand-red); }
  .newsletter-tagline { position: absolute; left: 11px; top: 418px; width: 205px; height: 45px; background: var(--charcoal); color: var(--ink-light); text-align: center; font-size: 13px; line-height: 1.3; padding-top: 5px; text-transform: uppercase; letter-spacing: 0.02em; }

  /* Shared band */
  .band { position: absolute; left: 0; width: 100%; background: var(--charcoal); border-top: 5px solid var(--brand-red); }

  .envelope-back { left: 275px; top: 39px; width: 330px; height: 155px; }
  .envelope-back .band { top: 75px; height: 80px; }
  .band .wordmark { position: absolute; left: 14px; top: 10px; font-size: 11px; color: var(--ink-light); }
  .band .contact { position: absolute; left: 22px; top: 40px; font-size: 4px; color: var(--ink-light); }
  .band .contact svg { fill: var(--ink-light); }

  .envelope-front { left: 275px; top: 213px; width: 330px; height: 154px; }
  .envelope-flap { position: absolute; left: 0; top: 0; }

  .comp-slip { left: 275px; top: 391px; width: 294px; height: 139px; }
  .comp-slip .band { top: 76px; height: 63px; }
  .comp-slip .band .contact { top: 36px; }
  .comp-greeting { position: absolute; right: 14px; top: 20px; font-family: "Yellowtail", "Brush Script MT", cursive; font-size: 14px; color: var(--brand-red); }

  .letterhead { left: 623px; top: 42px; width: 326px; height: 461px; }
  .letterhead .wordmark { position: absolute; left: 32px; top: 14px; font-size: 13px; }
  .letterhead .contact { position: absolute; left: 232px; top: 17px; font-size: 3.4px; font-weight: 500; }
  .letterhead .band { bottom: 0; height: 14px; }

  .card-front { left: 970px; top: 62px; width: 207px; height: 125px; }
  .card-person { position: absolute; left: 14px; top: 11px; }
  .card-name { font-size: 9px; font-weight: 500; color: var(--brand-red); }
  .card-role { font-size: 5px; color: var(--charcoal); }
  .card-front .wordmark { position: absolute; left: 113px; top: 14px; font-size: 10px; }
  .card-front .contact { position: absolute; left: 14px; top: 79px; font-size: 5.5px; }

  .card-back { left: 970px; top: 210px; width: 204px; height: 124px; }
  .card-back-panel { position: absolute; left: 0; top: 0; width: 100%; height: 102px; background: var(--charcoal); }
  .card-back .wordmark { position: absolute; left: 38px; top: 14px; font-size: 17px; color: var(--ink-light); }
  .card-tagline { position: absolute; left: 0; width: 100%; top: 106px; text-align: center; font-size: 8.5px; color: var(--brand-red); }
</style>
</head>
<body>

<svg width="0" height="0" style="position:absolute" aria-hidden="true">
  <symbol id="icon-phone" viewBox="0 0 10 10"><path d="M2 1h2l1 2-1 1c.5 1 1 1.5 2 2l1-1 2 1v2c-4 1-8-3-7-7z"/></symbol>
  <symbol id="icon-web" viewBox="0 0 10 10"><path d="M5 0a5 5 0 1 0 0 10A5 5 0 0 0 5 0zm0 1.2c.7.6 1.2 1.6 1.3 2.8H3.7C3.8 2.8 4.3 1.8 5 1.2zM1.3 5.2h2.4c.1 1.3.6 2.5 1.3 3.4A3.9 3.9 0 0 1 1.3 5.2zm5 0h2.4A3.9 3.9 0 0 1 5 8.6c.7-.9 1.2-2.1 1.3-3.4z"/></symbol>
  <symbol id="icon-mail" viewBox="0 0 10 10"><path d="M0 2h10v6H0zM1 3l4 3 4-3v-.2H1z"/></symbol>
  <symbol id="icon-pin" viewBox="0 0 10 10"><path d="M5 0a3.5 3.5 0 0 0-3.5 3.5C1.5 6 5 10 5 10s3.5-4 3.5-6.5A3.5 3.5 0 0 0 5 0zm0 2.2a1.3 1.3 0 1 1 0 2.6 1.3 1.3 0 0 1 0-2.6z"/></symbol>
</svg>

<!-- Newsletter cover -->
<section class="piece newsletter" aria-label="Newsletter cover">
  <svg class="newsletter-hero" viewBox="0 0 205 200" aria-hidden="true">
    <path d="M0 0H205V198C190 168 150 151 102.5 151S15 168 0 198Z" fill="var(--brand-red)"/>
  </svg>
  <div class="wordmark"><span class="wm-top">The</span><span>Lantern Yard</span></div>
  <p class="newsletter-service">Sundays @ 10am</p>
  <p class="newsletter-date">Sunday, 12 Oct 2014</p>
  <p class="newsletter-tagline">A place of hope<br>belonging and worship</p>
  <div class="newsletter-frame"></div>
</section>

<!-- Envelope back -->
<section class="piece envelope-back" aria-label="Envelope back">
  <div class="band">
    <div class="wordmark"><span class="wm-top">The</span><span>Lantern Yard</span></div>
    <ul class="contact">
      <li><svg width="4" height="4"><use href="#icon-mail"/></svg>office@kerrowbychapel.org.nz</li>
      <li><svg width="4" height="4"><use href="#icon-pin"/></svg>PO Box 53081, Kerrowby, Auckland 1832</li>
    </ul>
  </div>
</section>

<!-- Envelope front -->
<section class="piece envelope-front" aria-label="Envelope front">
  <svg class="envelope-flap" width="330" height="60" viewBox="0 0 330 60" aria-hidden="true">
    <path d="M0 0H330C322 20 320 52 300 59H30C10 52 8 20 0 0Z" fill="var(--charcoal)"/>
  </svg>
</section>

<!-- With compliments slip -->
<section class="piece comp-slip" aria-label="With compliments slip">
  <div class="band">
    <div class="wordmark"><span class="wm-top">The</span><span>Lantern Yard</span></div>
    <ul class="contact">
      <li><svg width="4" height="4"><use href="#icon-mail"/></svg>office@kerrowbychapel.org.nz</li>
      <li><svg width="4" height="4"><use href="#icon-pin"/></svg>PO Box 53081, Kerrowby, Auckland 1832</li>
    </ul>
    <p class="comp-greeting">With Compliments</p>
  </div>
</section>

<!-- Letterhead -->
<section class="piece letterhead" aria-label="Letterhead">
  <div class="wordmark"><span class="wm-top">The</span><span>Lantern Yard</span></div>
  <ul class="contact">
    <li><svg width="3" height="3"><use href="#icon-phone"/></svg>09 361 4507</li>
    <li><svg width="3" height="3"><use href="#icon-web"/></svg>www.kerrowbychapel.org.nz</li>
    <li><svg width="3" height="3"><use href="#icon-mail"/></svg>office@kerrowbychapel.org.nz</li>
    <li><svg width="3" height="3"><use href="#icon-pin"/></svg>PO Box 53081, Kerrowby, Auckland 1832</li>
  </ul>
  <div class="band"></div>
</section>

<!-- Business card front -->
<section class="piece card-front" aria-label="Business card front">
  <div class="card-person">
    <p class="card-name">Reid Halvorsen</p>
    <p class="card-role">Designation</p>
  </div>
  <div class="wordmark"><span class="wm-top">The</span><span>Lantern Yard</span></div>
  <ul class="contact">
    <li><svg width="5" height="5"><use href="#icon-phone"/></svg>09 361 4507</li>
    <li><svg width="5" height="5"><use href="#icon-web"/></svg>www.kerrowbychapel.org.nz</li>
    <li><svg width="5" height="5"><use href="#icon-mail"/></svg>office@kerrowbychapel.org.nz</li>
    <li><svg width="5" height="5"><use href="#icon-pin"/></svg>PO Box 53081, Kerrowby, Auckland 1832</li>
  </ul>
</section>

<!-- Business card back -->
<section class="piece card-back" aria-label="Business card back">
  <div class="card-back-panel">
    <div class="wordmark"><span class="wm-top">The</span><span>Lantern Yard</span></div>
  </div>
  <p class="card-tagline">a place of hope, belonging and worship</p>
</section>

</body>
</html>
```